law firm business cards

I need a business card using my existing logo. Two sided is best because there is a lot of information that needs to go on the card. Use the same general color scheme as logo, but I need one set with the blue background of my website (www.halvorsenlawgrp.com), and one set with white background (to see which one I like best).

Information that must be on there:
Trevor J. Halvorsen
Board Certified Civil Trial Specialist
738 Brinkley Ave., Suite 640
Raleigh, NC 27601

T 919-555-0143
F 919-555-0176

www.halvorsenlawgrp.com
trevor@halvorsenlawgrp.com

Personal Injury | Criminal Law (to separate the two, pls use a bullet point or pipeline symbol "|"

If there is a way to work in the CPRS logo (maybe at the bottom somewhere), put it in, but don't let it detract from the main logo too much.

Also, if there is a way to work it in, put in somewhere: Former Insurance Company Attorney | Former Criminal Prosecutor (to separate the two, pls use a bullet point or pipeline symbol "|"

```html
<!DOCTYPE html>
<html lang="en">
<head>
<meta charset="utf-8">
<title>Halvorsen Law – Business Cards</title>
<link href="https://fonts.googleapis.com/css2?family=Cinzel:wght@500;600&family=Open+Sans:wght@400;600&display=swap" rel="stylesheet">
<style>
  :root {
    --navy: #1f3a6b;
    --navy-deep: #18305a;
    --sky: #7fa6d8;
    --sky-pale: #b9cde8;
    --ink: #2b2f3a;
    --paper: #f6f7f9;
    --stage: #e9ebee;
    --white: #ffffff;
  }
  * { margin: 0; padding: 0; box-sizing: border-box; }
  html, body { width: 1200px; height: 469px; overflow: hidden; }
  body { background: var(--stage); position: relative; font-family: "Open Sans", Arial, sans-serif; }

  .card {
    position: absolute; top: 102px; width: 466px; height: 266px;
    box-shadow: 0 3px 10px rgba(0,0,0,.18);
  }
  .card--front { left: 106px; background: linear-gradient(135deg, var(--white), var(--paper)); overflow: hidden; }
  .card--back { left: 584px; background: var(--navy); }

  .edge-stripe { position: absolute; left: 0; top: 0; width: 9px; height: 100%; background: var(--navy); }
  .edge-stripe span { position: absolute; left: 3px; width: 6px; height: 38px; background: var(--sky-pale); }

  .brand { position: absolute; display: flex; align-items: center; gap: 14px; }
  .brand-mark { width: 38px; height: 38px; }
  .brand-name {
    font-family: "Cinzel", Georgia, serif; font-weight: 600; font-size: 36px; line-height: 1;
    letter-spacing: .5px;
  }
  .card--front .brand { left: 70px; top: 42px; }
  .card--front .brand-mark { background: var(--navy); }
  .card--front .brand-name { color: var(--navy); }
  .card--back .brand { left: 28px; top: 30px; }
  .card--back .brand-mark { background: var(--white); }
  .card--back .brand-name { color: var(--white); }

  .person-name {
    position: absolute; left: 0; width: 100%; top: 144px; text-align: center;
    font-family: "Cinzel", Georgia, serif; font-weight: 500; font-size: 21px; color: var(--navy); letter-spacing: 1px;
  }
  .rule { position: absolute; height: 1px; background: var(--sky-pale); }
  .card--front .rule { left: 24px; width: 420px; top: 175px; }

  .address { position: absolute; right: 240px; top: 197px; text-align: right; font-size: 10.5px; line-height: 18px; color: var(--ink); }
  .address .title { font-weight: 600; color: var(--navy); }
  .divider { position: absolute; left: 239px; top: 198px; width: 1px; height: 50px; background: var(--sky-pale); }
  .contact { position: absolute; left: 256px; top: 197px; font-size: 10.5px; line-height: 16px; color: var(--ink); }
  .contact b { font-weight: 600; color: var(--navy); }
  .contact .web { margin-top: 6px; font-weight: 600; color: var(--navy); letter-spacing: .6px; }

  .practice { position: absolute; left: 28px; top: 170px; display: grid; grid-template-columns: 108px auto; row-gap: 4px; list-style: none; }
  .practice li { font-size: 10.5px; color: var(--white); display: flex; align-items: center; gap: 6px; }
  .practice li::before { content: ""; width: 6px; height: 6px; border-radius: 50%; background: var(--sky); }
  .card--back .rule { left: 16px; width: 447px; top: 220px; background: rgba(185,205,232,.55); }
  .back-web { position: absolute; left: 26px; top: 233px; font-size: 10.5px; font-weight: 600; letter-spacing: 3.6px; color: var(--white); }
  .cert-badge { position: absolute; left: 373px; top: 170px; width: 84px; height: 84px; }
</style>
</head>
<body>
  <section class="card card--front">
    <div class="edge-stripe"><span style="top:0"></span><span style="top:48px"></span><span style="top:96px"></span><span style="top:144px"></span><span style="top:192px"></span><span style="top:240px"></span></div>
    <div class="brand"><div class="brand-mark"></div><div class="brand-name">Halvorsen Law</div></div>
    <h1 class="person-name">Trevor J. Halvorsen</h1>
    <div class="rule"></div>
    <div class="address">
      <div class="title">Board Certified Civil Trial Specialist</div>
      <div>738 Brinkley Ave., Suite 640</div>
      <div>Raleigh, NC 27601</div>
    </div>
    <div class="divider"></div>
    <div class="contact">
      <div><b>T:</b> 919-555-0143, &nbsp;<b>F:</b> 919-555-0176</div>
      <div><b>E:</b> trevor@halvorsenlawgrp.com</div>
      <div class="web">www.halvorsenlawgrp.com</div>
    </div>
  </section>

  <section class="card card--back">
    <div class="brand"><div class="brand-mark"></div><div class="brand-name">Halvorsen Law</div></div>
    <ul class="practice">
      <li>Personal Injury</li><li>Former Insurance Company Attorney</li>
      <li>Criminal Law</li><li>Former Criminal Prosecutor</li>
    </ul>
    <div class="rule"></div>
    <div class="back-web">www.halvorsenlawgrp.com</div>
    <svg class="cert-badge" viewBox="0 0 84 84" role="img" aria-label="CPRS certification badge">
      <circle cx="42" cy="42" r="40" fill="#ffffff"/>
      <circle cx="42" cy="42" r="33" fill="none" stroke="#1f3a6b" stroke-width="1.5"/>
    </svg>
  </section>
</body>
</html>
```